KVT Business Cards

We require business cards for our business. We would like a matte black back to the card, with our logo centred in the middle. The front side of the card is open to design.

Target Market(s)

Clients looking for legal services (professional)

Industry/Entity Type

Legal

Contact Information for Business Card

Boris Telemark
Partner
Mobile: 0438 715 642
Email: boris@kvtlaw.co
Website: www.kvtlaw.co
Level 3, 118 Wexbury Street
Sydney NSW 2000

Font styles to use
Other font styles liked:
• Avenir

Colors
f04a50
ffffff
1b1b1b

Requirements
Must have
• Black back with logo included in the centre of the card.
• Our font is Avenir.

```html
<!DOCTYPE html>
<html lang="en">
<head>
<meta charset="utf-8">
<title>KVT Business Cards</title>
<link href="https://fonts.googleapis.com/css2?family=Nunito+Sans:wght@400;600;800&display=swap" rel="stylesheet">
<style>
  :root {
    --stage: #1f1f1f;
    --card: #141414;
    --card-edge: #0c0c0c;
    --crimson: #cf1f4a;
    --crimson-deep: #a81a3c;
    --white: #ffffff;
    --rule: #e8e8e8;
  }
  * { box-sizing: border-box; margin: 0; padding: 0; }
  html, body { width: 1200px; height: 1200px; overflow: hidden; }
  body {
    background: radial-gradient(circle at 50% 40%, #2c2c2c 0%, var(--stage) 60%, #121212 100%);
    font-family: "Nunito Sans", sans-serif;
    color: var(--white);
    position: relative;
  }
  .card {
    position: absolute;
    left: 150px;
    width: 900px;
    height: 515px;
    border-radius: 26px;
    background: linear-gradient(160deg, #1c1c1c 0%, var(--card) 50%, var(--card-edge) 100%);
    box-shadow: 0 18px 40px rgba(0,0,0,0.55);
    overflow: hidden;
  }
  .card-back { top: 50px; }
  .card-front { top: 630px; }

  .brand { display: flex; align-items: center; gap: 28px; }
  .brand-square { width: 70px; height: 70px; background: var(--crimson); }
  .brand-name {
    font-weight: 800;
    font-size: 44px;
    line-height: 1.0;
    letter-spacing: 1px;
    text-transform: uppercase;
    color: var(--white);
  }
  .card-back .brand {
    position: absolute;
    left: 50%; top: 50%;
    transform: translate(-50%, -50%);
  }
  .card-front .brand { position: absolute; left: 70px; top: 60px; }
  .card-front .brand-square { width: 60px; height: 60px; }
  .card-front .brand-name { font-size: 40px; }

  .holder { position: absolute; right: 60px; top: 270px; text-align: right; }
  .holder-name {
    color: var(--crimson);
    font-weight: 800;
    font-size: 34px;
    letter-spacing: 1px;
    text-transform: uppercase;
  }
  .holder-role { font-weight: 800; font-size: 22px; letter-spacing: 1px; }

  .divider {
    position: absolute; left: 60px; right: 60px; top: 352px;
    height: 1.5px; background: var(--rule);
  }

  .contact { position: absolute; left: 60px; top: 368px; list-style: none; }
  .contact li {
    display: flex; align-items: center; gap: 12px;
    font-size: 20px; margin-bottom: 6px;
  }
  .contact svg { width: 20px; height: 20px; flex: none; }

  .address {
    position: absolute; right: 60px; top: 368px;
    text-align: right; font-size: 20px; line-height: 1.35;
  }

  .web-band {
    position: absolute; left: 0; right: 0; bottom: 0; height: 64px;
    background: linear-gradient(90deg, var(--crimson-deep), var(--crimson));
    display: flex; align-items: center; justify-content: center;
  }
  .web-band a {
    color: var(--white); text-decoration: none;
    font-weight: 800; font-size: 22px; letter-spacing: 1.5px;
  }
</style>
</head>
<body>

<section class="card card-back" aria-label="Card back">
  <div class="brand">
    <span class="brand-square"></span>
    <span class="brand-name">Kerrigan<br>Telemark<br>Legal</span>
  </div>
</section>

<section class="card card-front" aria-label="Card front">
  <div class="brand">
    <span class="brand-square"></span>
    <span class="brand-name">Kerrigan<br>Telemark<br>Legal</span>
  </div>

  <div class="holder">
    <p class="holder-name">Boris Telemark</p>
    <p class="holder-role">PARTNER</p>
  </div>

  <div class="divider"></div>

  <ul class="contact">
    <li>
      <svg viewBox="0 0 20 20" aria-hidden="true">
        <rect x="5" y="1" width="10" height="18" rx="2" fill="none" stroke="var(--crimson)" stroke-width="2"/>
        <rect x="8" y="15" width="4" height="2" fill="var(--crimson)"/>
      </svg>
      0438 715 642
    </li>
    <li>
      <svg viewBox="0 0 20 20" aria-hidden="true">
        <rect x="1" y="4" width="18" height="12" fill="var(--crimson)"/>
        <path d="M1 4 L10 11 L19 4" fill="none" stroke="var(--card)" stroke-width="1.5"/>
      </svg>
      boris@kvtlaw.co
    </li>
  </ul>

  <address class="address" style="font-style:normal">
    Level 3, 118 Wexbury Street<br>
    Sydney NSW 2000
  </address>

  <div class="web-band">
    <a href="#">WWW.KVTLAW.CO</a>
  </div>
</section>

</body>
</html>
```